Entrepreneur needs a business card design

I need a business card to name my three companies, as well as contact information.
I'm open on design and color and it can be plain or complex. I'm open on colors but I think I prefer something somewhat formal but fun as well.
I'm open on whether the background is plain or has design in it. I don't have company logos.
Target Market(s)
Auto dealers, realtors and property managers
Industry/Entity Type
Business
Contact Information for Business Card
HOLLISTER FAMILY PROPERTIES, LLC
HOLLISTER PUBLISHING, LLC
LOTMASTER CONSULTING, LLC
Ned Hollister
2847 W. Tamarack Ave. #310
Boise, Idaho 83611-2905
208-514-3092
ned@holl5x.example

```html
<!DOCTYPE html>
<html lang="en">
<head>
<meta charset="utf-8">
<title>Hollister Family Properties – Business Card</title>
<link rel="stylesheet" href="https://fonts.googleapis.com/css2?family=Cinzel:wght@400;500&family=PT+Sans&display=swap">
<style>
  :root {
    --page: #d9d7d4;
    --card: #fbfbfa;
    --band-dark: #1f1c1b;
    --band-mid: #3b3735;
    --ink: #1a1a1a;
    --ink-light: #f4f3f1;
  }
  * { margin: 0; padding: 0; box-sizing: border-box; }
  html, body {
    width: 1200px;
    height: 780px;
    overflow: hidden;
    background: var(--page);
  }
  .card {
    position: absolute;
    left: 75px;
    top: 90px;
    width: 1050px;
    height: 600px;
    background: var(--card);
    box-shadow: 0 6px 24px rgba(0,0,0,0.18);
  }
  .company-title {
    position: absolute;
    left: 120px;
    top: 112px;
    font-family: "Cinzel", "Times New Roman", serif;
    font-weight: 500;
    font-size: 42px;
    letter-spacing: 1px;
    color: var(--ink);
  }
  .entity-band {
    position: absolute;
    left: 0;
    top: 215px;
    width: 100%;
    height: 190px;
    background: linear-gradient(90deg, var(--band-dark) 0%, var(--band-mid) 55%, var(--band-dark) 100%);
  }
  .entity-tag {
    position: absolute;
    left: 120px;
    top: 68px;
    display: flex;
    align-items: center;
    gap: 18px;
    font-family: "Cinzel", "Times New Roman", serif;
    font-size: 30px;
    line-height: 1;
    letter-spacing: 0.5px;
    color: var(--ink-light);
  }
  .entity-square {
    width: 44px;
    height: 44px;
    background: var(--ink-light);
  }
  .entity-list {
    position: absolute;
    left: 440px;
    top: 34px;
    list-style: none;
    font-family: "Cinzel", "Times New Roman", serif;
    font-size: 30px;
    line-height: 1.08;
    letter-spacing: 0.5px;
    color: var(--ink-light);
  }
  .address {
    position: absolute;
    left: 120px;
    top: 452px;
    font-family: "PT Sans", "Helvetica", sans-serif;
    font-style: normal;
    font-size: 29px;
    line-height: 1.2;
    color: var(--ink);
  }
  .contact {
    position: absolute;
    left: 640px;
    top: 425px;
    list-style: none;
    font-family: "PT Sans", "Helvetica", sans-serif;
    font-size: 29px;
    line-height: 1.3;
    color: var(--ink);
  }
  .contact li { display: flex; align-items: center; gap: 16px; }
  .contact svg { width: 30px; height: 24px; fill: var(--ink); }
</style>
</head>
<body>
  <section class="card">
    <h1 class="company-title">HOLLISTER FAMILY PROPERTIES</h1>

    <div class="entity-band">
      <div class="entity-tag">
        <span class="entity-square" aria-hidden="true"></span>
        <span>LLC</span>
      </div>
      <ul class="entity-list">
        <li>HOLLISTER PUBLISHING</li>
        <li>LOTMASTER CONSULTING</li>
        <li>NED HOLLISTER</li>
      </ul>
    </div>

    <address class="address">
      2847 W. Tamarack Ave.<br>
      #310 Boise, Idaho 83611-2905
    </address>

    <ul class="contact">
      <li>
        <svg viewBox="0 0 30 24" aria-hidden="true">
          <path d="M3 8c0-3 5-5 12-5s12 2 12 5v2h-6V8c-2-1-10-1-12 0v2H3z"/>
          <path d="M8 11h14l4 11H4z"/>
          <circle cx="15" cy="16" r="3" fill="#fbfbfa"/>
        </svg>
        <span>208-514-3092</span>
      </li>
      <li>
        <svg viewBox="0 0 30 24" aria-hidden="true">
          <path d="M2 3h26v18H2z"/>
          <path d="M3 4l12 10L27 4" fill="none" stroke="#fbfbfa" stroke-width="2"/>
        </svg>
        <span>ned@holl5x.example</span>
      </li>
    </ul>
  </section>
</body>
</html>
```